website for local kavenda practicioner and yoga teacher trainer

The website should function primarily as:
A place where people can discover Kavenda and book sessions.
A central hub connecting all of my work.
A professional home that reflects my personality and approach.
Website design for Liesbet Oonwerk — Kavenda® Structural Integration practitioner, movement educator, yoga teacher and teacher trainer.
A website that can grow with future projects.
The website should feel: Warm, Human, Invitational, Professional, Accessible, Intelligent, Calm, Clear, Playful, Exploratory, Trustworthy
Avoid: New age aesthetics, Mystical clichés, Excessive spirituality, ”Guru" vibes, Overly clinical design, Corporate wellness branding, Busy layouts
Think: modern, grounded, curious and real.
My work combines three interconnected areas:
1.Bodywork: Touch, structure, awareness and one-on-one support.
2. Movement: Yoga, Pilates and embodied movement.
3. Education: Teacher trainings, workshops and continued learning.
Underlying values:
Curiosity over certainty
Possibility over perfection
Complexity without overwhelm
Science and lived experience together
Exploration rather than dogma
Human beings before methods
The primary goal of the website is to introduce people to Kavenda® Structural Integration and make it easy for them to:
Understand what Kavenda is
Discover whether it might be relevant for them
Learn what to expect from a session
Book an appointment
Booking should always feel visible and easy.
Secondary Goal: Present all other aspects of my work in one coherent place:
Yoga classes
Pilates classes
Teacher trainings
Workshops
Retreats
One-on-one movement sessions
Collaborations with studios
Website Structure
1: HOME
1.1.Hero Section: Large welcoming image
1.2 Two Main Pathways
- Bodywork: Kavenda® Structural Integration
- Movement & Education: Yoga, Pilates, trainings, workshops and retreats
- About Preview: Small introduction with portrait. + Button:
Read More
1.3 Current Events / What's Coming Up: Upcoming trainings, workshops and retreats. (This section should be easy to update)
1.4. Contact / Newsletter: Simple contact information
2: Kavenda® Structural Integration
What is Kavenda?
For whom is it?
What does a session look like?
FAQ
Prices
Booking
Future possibility:
Kaven Movement sessions
3: Movement
- Introductory text.
- Studio Classes (link to “my home base” - > local yoga studio)
- One-to-One Sessions: booking option (this is small; not a key aspect I want to promote)
- Workshops/ Retreats / Teacher Trainings => This section should be flexible and easy to update. Visitors should be able to click into specific offerings.
4. Events
Dynamic page for: Teacher trainings, Retreats, Workshops (see section in movement; here more elaborate)
Each event should contain: Image, Short description, Location, Date, Button for more information. (Linking to hosting studio/location)
5. Work With Me
For studios, organisations and teacher training schools.
Examples: Guest teaching, Workshops, Anatomy, Sequencing, Teacher development , Continuing education -> Clear call-to-action.
Call to action!!=> Book a Session
Prominent button in the navigation.
Footer:
- About Me: Longer biography (6th page)
Personal story and background.
- Testimonials (7th page): Separate page containing testimonials from:
Kavenda clients
Students
Teacher trainees
- Contact: 8th page
Visual Direction
Natural textures. Lots of white space.Editorial feeling.Professional photography.Simple navigation.
Less "wellness influencer.” More:Thoughtful, Contemporary, Timeless, Grounded, Human
Photography should show:
Teaching
Hands-on work
Natural movement
Real interaction
Simplicity
Avoid stereotypical yoga imagery and overly spiritual aesthetics.
Keywords
Warm. Curious. Human. Professional. Embodied. Intelligent. Accessible. Playful. Grounded. Exploratory. Real.
Inspiration / Core Message
Helping people feel more at home in their bodies through touch, movement and education.
The website should communicate that these are not separate services, but different expressions of the same intention:
Bodywork • Movement • Education.
Colours:
light orange/beige: e3d5c4
light orange/off white: f9f7f3
gray azure: 556b78
orange: d07b5a
grey orange: c09f80
dark grey: 3e3e3e
dark gray cyan 2f4f4f
gray green colour: a7c4a0
Fonts: Montserrat and Poppins + raleway
In added documents a try out idea of a website + logo. I will mainly use the logo with diffrent colours (image next to text).
My audience consists of people who want to feel more at home in their bodies and who appreciate a thoughtful, grounded and human approach to movement, touch and education. (30-65yo)
wellbeing
5+ page
- montserrat, poppins, raleway

```html
<!DOCTYPE html>
<html lang="en">
<head>
<meta charset="utf-8">
<title>Liesbet Oonwerk — Movement, Breath and Touch</title>
<link href="https://fonts.googleapis.com/css2?family=Raleway:wght@200;300;400&family=Poppins:wght@300;400;500&family=Cormorant+Garamond:ital,wght@1,400&display=swap" rel="stylesheet">
<style>
:root{
  --board:#353638;
  --paper:#f9f7f3;
  --sand:#e3d5c4;
  --band:#e0d5ca;
  --azure:#556b78;
  --orange:#d07b5a;
  --grey-orange:#c09f80;
  --ink:#3e3e3e;
  --cyan:#3f5753;
  --green:#a7c4a0;
}
*{box-sizing:border-box;margin:0;padding:0}
html,body{width:1200px;height:1200px;overflow:hidden;background:var(--board)}
body{position:relative;font-family:'Poppins',sans-serif;color:var(--ink)}
.page{position:absolute;width:649px;background:var(--paper);transform-origin:0 0;transform:scale(0.6211);overflow:hidden;font-size:6px;line-height:1.4}
.page--home{left:173px;top:91px;height:1637px}
.page--story{left:624px;top:91px;height:1261px}
.abs{position:absolute}
.serif{font-family:'Cormorant Garamond',serif;font-style:italic;color:var(--orange)}
.display{font-family:'Raleway',sans-serif;font-weight:300;color:var(--ink);letter-spacing:-.01em}
.eyebrow{font-size:3.6px;letter-spacing:.2em;text-transform:uppercase;color:var(--orange);display:flex;align-items:center;gap:5px}
.eyebrow::before{content:"";width:14px;height:.6px;background:var(--orange)}
.body{font-size:6.6px;line-height:1.7;color:#4a4a4a}
.photo{position:absolute}
.blob{position:absolute;border-radius:50%;background:var(--green);opacity:.5}
.btn{position:absolute;border-radius:20px;font-size:4.4px;letter-spacing:.18em;text-transform:uppercase;display:flex;align-items:center;justify-content:center;font-weight:500}
.btn--dark{background:var(--azure);color:#fff}
.btn--line{border:.8px solid var(--orange);color:var(--orange)}
.link{font-size:4.4px;letter-spacing:.18em;text-transform:uppercase;color:var(--orange);border-bottom:.6px solid var(--orange);padding-bottom:2px;font-weight:500}
.list{list-style:none;font-size:4.8px;color:#555;line-height:2.25}
.list li::before{content:"";display:inline-block;width:9px;height:.6px;background:var(--orange);margin-right:5px;vertical-align:middle}
.num{font-family:'Raleway',sans-serif;font-weight:300;font-size:9px;color:var(--orange)}
.tag{font-size:3.8px;letter-spacing:.2em;text-transform:uppercase;color:#777;line-height:1.4}
.logo{display:flex;align-items:center;gap:4px;font-size:6.4px;line-height:1;color:var(--ink)}
.logo i{width:7px;height:7px;border-radius:50%;background:var(--ink)}
.nav{display:flex;gap:12px;font-size:4.6px;line-height:1}
.nav a{color:#555;text-decoration:none}
.card{position:absolute;top:716px;width:163px;height:132px;background:var(--paper);padding:16px 16px}
.card .q{color:var(--orange);font-size:8px;line-height:1;font-family:'Cormorant Garamond',serif}
.card .t{font-size:5.2px;line-height:1.8;color:#4a4a4a;margin-top:8px}
.card .who{position:absolute;left:16px;right:16px;bottom:16px;border-top:.6px solid #ddd;padding-top:9px;display:flex;align-items:center;gap:6px;font-size:4.2px;line-height:1.4}
.card .av{width:15px;height:15px;border-radius:50%;background:#d5dccf;display:flex;align-items:center;justify-content:center;font-size:4px;color:#666;flex:none}
.card .who b{font-weight:500;display:block;font-size:4.6px;color:var(--ink)}
.card .who span{letter-spacing:.15em;text-transform:uppercase;color:#888;font-size:3.6px}
.card .who em{margin-left:auto;font-style:normal;color:var(--orange)}
.fact{font-size:3.6px;letter-spacing:.2em;text-transform:uppercase;color:#a9b8b4}
.fact + p{font-family:'Raleway',sans-serif;font-size:7.2px;color:#e9ece8;margin-top:6px;line-height:1.5}
.stat .display{font-size:8px;line-height:1.3}
</style>
</head>
<body>

<!-- Home page -->
<section class="page page--home">
  <div class="abs logo" style="left:72px;top:17px"><i></i>Liesbet Oonwerk</div>
  <nav class="abs nav" style="left:232px;top:18px"><a>Practice</a><a>Yoga</a><a>Kavenda</a><a>Retreats</a><a>About</a><a>Journal</a></nav>
  <div class="btn btn--dark" style="left:509px;top:12px;width:73px;height:16px">Book a session →</div>

  <div class="abs eyebrow" style="left:72px;top:89px">Leiden · The Netherlands</div>
  <h1 class="abs display" style="left:72px;top:104px;font-size:33px;line-height:1.03">A quiet practice<br>of <span class="serif">movement</span>,<br>breath and touch.</h1>
  <p class="abs body" style="left:72px;top:218px;width:225px;font-size:6.2px">Yoga, Kavenda® Structural Integration, trainings and retreats with Liesbet Oonwerk — for more ease, resilience, and connection in the body you already are.</p>
  <div class="btn btn--dark" style="left:72px;top:269px;width:93px;height:21px">Book a session →</div>
  <div class="btn btn--line" style="left:171px;top:269px;width:116px;height:21px">Explore the practice ↓</div>
  <div class="abs" style="left:72px;top:311px;width:222px;height:.6px;background:#ddd"></div>
  <div class="abs stat" style="left:72px;top:326px"><div class="display">15+</div><div class="tag" style="font-size:3.4px">Years teaching</div></div>
  <div class="abs stat" style="left:149px;top:326px"><div class="display">EN · NL · FR</div><div class="tag" style="font-size:3.4px">Languages</div></div>
  <div class="abs stat" style="left:227px;top:326px"><div class="display">1:1 &amp; group</div><div class="tag" style="font-size:3.4px">Sessions</div></div>

  <div class="blob" style="left:336px;top:45px;width:56px;height:56px"></div>
  <div class="photo" role="img" aria-label="Practitioner seated cross-legged in a sunlit studio" style="left:346px;top:55px;width:236px;height:295px;background:linear-gradient(120deg,#e9d6b8,#d7b88e 60%,#c9a57c)"></div>
  <div class="abs tag" style="left:346px;top:357px;font-size:3.6px">— Studio practice, autumn</div>
  <div class="abs tag" style="left:560px;top:357px;font-size:3.6px;color:var(--orange)">01 / 04</div>

  <div class="abs" style="left:58px;top:394px;width:540px;height:22px;border-top:.6px solid #ddd;border-bottom:.6px solid #ddd;display:flex;justify-content:space-between;align-items:center;padding:0 14px">
    <span class="tag">• Yoga</span><span class="tag">• Kavenda® S.I.</span><span class="tag">• Trainings</span><span class="tag">• Retreats</span><span class="tag">• 1:1 Sessions</span>
  </div>

  <div class="abs" style="left:0;top:452px;width:649px;height:233px;background:var(--band)"></div>
  <div class="abs eyebrow" style="left:72px;top:502px">The practice</div>
  <h2 class="abs display" style="left:72px;top:515px;font-size:21px;line-height:1.2">Bodies are <span class="serif">plastic</span> to<br>the intent of life.</h2>
  <div class="abs body" style="left:319px;top:506px;width:264px;font-size:6px">
    <p>At the heart of my work is the belief that our bodies are not machines to optimise, but living, sensing systems with their own intelligence, adaptability, and possibility.</p>
    <p style="margin-top:8px">Through movement, breath, touch, and attention we build greater capacity, support and grounding — not by forcing ourselves into fixed shapes or ideals, but by learning to listen more closely to the body and its changing needs.</p>
    <p style="margin-top:8px">From this place of connection, new possibilities for movement, expression, and being begin to open up. We find not a single "better" way to live, but more freedom, responsiveness, and choice.</p>
  </div>

  <div class="abs eyebrow" style="left:72px;top:735px">Three threads</div>
  <h2 class="abs display" style="left:72px;top:745px;font-size:13px">Yoga · Bodywork · Retreats</h2>
  <p class="abs body" style="left:409px;top:744px;width:175px;font-size:4.8px;line-height:1.6">Three meeting points with the same underlying work — listening to the body and giving it room to find its own way.</p>

  <div class="photo" role="img" aria-label="Group yoga class in a warm, sunlit studio" style="left:72px;top:787px;width:287px;height:229px;background:linear-gradient(135deg,#efd3a8,#d9a870 55%,#b98b5e)"></div>
  <div class="blob" style="left:63px;top:987px;width:36px;height:36px"></div>
  <div class="abs" style="left:393px;top:820px;display:flex;align-items:center;gap:6px"><span class="num">01</span><span class="tag" style="color:var(--orange);font-size:3.4px">Movement as exploration</span></div>
  <h3 class="abs display" style="left:393px;top:839px;font-size:17px">Yoga</h3>
  <p class="abs body" style="left:393px;top:866px;width:190px;font-size:6px">A space to build strength, mobility, awareness, resilience — and a little more freedom in how we move and relate to ourselves. Classes weave together breath, anatomy, playfulness, challenge, rest and attention.</p>
  <ul class="abs list" style="left:393px;top:930px"><li>Group classes</li><li>Private sessions</li><li>Pilates &amp; therapeutic movement</li></ul>
  <span class="abs link" style="left:393px;top:974px">Explore yoga →</span>

  <div class="abs" style="left:72px;top:1098px;display:flex;align-items:center;gap:6px"><span class="num">02</span><span class="tag" style="color:var(--orange);font-size:3.4px">A collaborative process</span></div>
  <h3 class="abs display" style="left:72px;top:1115px;font-size:17px;line-height:1.15">Kavenda® Structural<br>Integration</h3>
  <p class="abs body" style="left:72px;top:1162px;width:195px;font-size:6px">A collaborative process exploring posture, movement, breath and our relationship to gravity through touch, awareness and movement. Sessions invite ease and adaptability — not by 'fixing' the body, but by creating space for new patterns to emerge.</p>
  <ul class="abs list" style="left:72px;top:1227px"><li>Treatment-table work</li><li>Standing &amp; movement exploration</li><li>Occasional Veldra Shiatsu</li></ul>
  <span class="abs link" style="left:72px;top:1271px">Explore Kavenda® →</span>
  <div class="photo" role="img" aria-label="Treatment table with linen, a bowl of oil and a plant" style="left:295px;top:1073px;width:287px;height:229px;background:linear-gradient(160deg,#a98a68,#d9c5a9 45%,#efe6d8)"></div>
  <div class="blob" style="left:555px;top:1274px;width:36px;height:36px"></div>

  <div class="photo" role="img" aria-label="Retreat terrace with olive trees overlooking the sea at sunset" style="left:72px;top:1360px;width:287px;height:229px;background:linear-gradient(170deg,#f0d6b0,#cfa77c 45%,#8f8a6c 75%,#b7a488)"></div>
  <div class="blob" style="left:63px;top:1561px;width:36px;height:36px"></div>
  <div class="abs" style="left:393px;top:1400px;display:flex;align-items:center;gap:6px"><span class="num">03</span><span class="tag" style="color:var(--orange);font-size:3.4px">Time away, in the body</span></div>
  <h3 class="abs display" style="left:393px;top:1418px;font-size:17px">Trainings &amp; retreats</h3>
  <p class="abs body" style="left:393px;top:1445px;width:190px;font-size:6px">Small-group trainings and retreats, locally in the Netherlands and abroad. A slower rhythm, longer practices, and the chance to live inside the work for a few days.</p>
  <ul class="abs list" style="left:393px;top:1497px"><li>Weekend intensives</li><li>International retreats</li><li>Teacher mentoring</li></ul>
  <span class="abs link" style="left:393px;top:1542px">Explore trainings →</span>
</section>

<!-- Story page -->
<section class="page page--story">
  <div class="abs" role="img" aria-label="Warm sunlit wall texture" style="left:0;top:0;width:649px;height:215px;background:linear-gradient(100deg,#dcc3a2,#e8d5bd 50%,#d2b692)"></div>
  <div class="abs eyebrow" style="left:0;width:649px;top:59px;justify-content:center">A note</div>
  <blockquote class="abs display" style="left:0;width:649px;top:74px;text-align:center;font-size:18.5px;line-height:1.23">“The body is not something to<br>perfect or control, but <span class="serif">something to<br>listen to</span>, explore, and live within.”</blockquote>
  <div class="abs tag" style="left:0;width:649px;top:154px;text-align:center;font-size:3.6px">— Liesbet Oonwerk</div>

  <div class="photo" role="img" aria-label="Portrait of the practitioner by a window" style="left:72px;top:263px;width:215px;height:269px;background:linear-gradient(110deg,#f2e7d4,#d8b48a 55%,#c9a07a)"></div>
  <div class="abs" style="left:252px;top:511px;width:42px;height:42px;border-radius:50%;background:#e8cfc4;opacity:.6"></div>
  <div class="abs tag" style="left:72px;top:539px;font-size:3.6px">— Liesbet · Leiden</div>
  <div class="abs eyebrow" style="left:318px;top:294px">About Liesbet</div>
  <h2 class="abs display" style="left:318px;top:305px;font-size:21px;line-height:1.2">Curiosity is what<br><span class="serif">connects</span> the work.</h2>
  <div class="abs body" style="left:318px;top:366px;width:262px;font-size:6px">
    <p>My background spans yoga, Pilates, Kavenda® Structural Integration, and years of training that continue to shape how I move, teach, touch, and relate to people.</p>
    <p style="margin-top:7px">The body is not something to perfect or control, but something to listen to, explore, and live within. Every body carries stories, habits, tensions, and possibilities — and every story moves.</p>
    <p style="margin-top:7px">Based in Leiden, I offer group classes, trainings, retreats and one-on-one sessions in movement and bodywork, both locally and abroad. I work in English, Dutch and French.</p>
  </div>
  <div class="btn btn--line" style="left:318px;top:497px;width:80px;height:17px;font-size:3.8px">More about me →</div>

  <div class="abs" style="left:0;top:593px;width:649px;height:305px;background:var(--band)"></div>
  <div class="abs eyebrow" style="left:72px;top:641px">In their words</div>
  <h2 class="abs display" style="left:72px;top:653px;font-size:17px;line-height:1.2">Quiet feedback,<br>from people who return.</h2>
  <p class="abs body" style="left:408px;top:676px;width:165px;font-size:4.6px;line-height:1.6">A small selection from students, clients and retreat guests across the Netherlands and beyond.</p>
  <div class="card" style="left:72px"><div class="q">“</div><p class="t">Liesbet holds a room with a rare quality of attention. I left her sessions feeling more honestly inside my body than I had in years.</p><div class="who"><div class="av">AD</div><div><b>Anouk D.</b><span>Weekly yoga student · Leiden</span></div><em>01</em></div></div>
  <div class="card" style="left:245px"><div class="q">“</div><p class="t">Kavenda with Liesbet changed how I stand, how I breathe — and somehow, how I think. It's the most lasting bodywork I've done.</p><div class="who"><div class="av">TL</div><div><b>Thomas L.</b><span>Kavenda 10-series · Amsterdam</span></div><em>02</em></div></div>
  <div class="card" style="left:418px"><div class="q">“</div><p class="t">The retreat felt like coming home to something. Slow, generous, and deeply intelligent in a way that never preaches.</p><div class="who"><div class="av">SM</div><div><b>Sofia M.</b><span>Provence retreat, 2025</span></div><em>03</em></div></div>

  <div class="abs" style="left:72px;top:947px;width:509px;height:208px;background:var(--cyan)"></div>
  <div class="abs eyebrow" style="left:103px;top:984px;color:#b7c2bf">Begin</div>
  <h2 class="abs display" style="left:103px;top:996px;font-size:21px;line-height:1.15;color:#f3f1ec">Step into<br>the <span class="serif" style="color:#e6c9b5">studio.</span></h2>
  <p class="abs body" style="left:103px;top:1058px;width:170px;font-size:4.8px;color:#d9dfdc;line-height:1.7">A first session is the simplest place to start — no commitment, just a quiet conversation in the body. I'll get back to you within two working days.</p>
  <div class="btn" style="left:103px;top:1100px;width:81px;height:18px;background:var(--orange);color:#fff;font-size:3.8px">Book a session →</div>
  <div class="btn" style="left:189px;top:1100px;width:71px;height:18px;border:.8px solid #8a9c98;color:#e6ebe8;font-size:3.8px">Ask a question</div>
  <div class="abs" style="left:457px;top:990px;width:.6px;height:135px;background:#5a726d"></div>
  <div class="abs" style="left:372px;top:1056px;width:180px;height:.6px;background:#5a726d"></div>
  <div class="abs" style="left:372px;top:993px"><div class="fact">Studio</div><p>Leiden, The<br>Netherlands</p></div>
  <div class="abs" style="left:466px;top:993px"><div class="fact">1:1 Session</div><p>75 min · €110</p></div>
  <div class="abs" style="left:372px;top:1066px"><div class="fact">Group class</div><p>Drop-in · €18</p></div>
  <div class="abs" style="left:466px;top:1066px"><div class="fact">Languages</div><p>EN · NL · FR</p></div>

  <div class="abs" style="left:58px;top:1207px;width:538px;height:.6px;background:#ddd"></div>
  <div class="abs logo" style="left:72px;top:1227px;font-size:6px"><i></i>Liesbet Oonwerk</div>
  <div class="abs tag" style="left:245px;top:1229px;font-size:3.6px;word-spacing:8px">hello@liesbetoonwerk.nl &nbsp; Photofeed &nbsp; Newsletter</div>
  <div class="abs" style="left:532px;top:1229px;font-size:3.6px;color:#999">© 2026 Liesbet Oonwerk</div>
</section>

</body>
</html>
```